TRELLWICK Construction Group business card for distribution

A business card detailing our services, with our phone number and email address.
- Groundworks / Foundations / Drainage
- Landscaping / Hard Landscaping / Patios / Decking
- Fencing
The card should include company logo and be in the same colours.

Target Market(s)
Domestic Houses
Industry/Entity Type
Construction
Contact Information for Business Card
Phone Number - 07931 258 904 / 07713829516. Email address: trellgroup@stonevane-mail.com
Font styles to use
Serif
Sans Serif
Colors
F0912C
F2A743
F7CA91
FBE8D2
FDF5EE
Requirements
Must have
- Contact numbers. Photos of past work. Company Logo

Nice to have
- Company Logo

```html
<!DOCTYPE html>
<html lang="en">
<head>
<meta charset="utf-8">
<title>Trellwick Construction Group – Business Card</title>
<link rel="stylesheet" href="https://fonts.googleapis.com/css2?family=Montserrat:wght@400;500;600;700&display=swap">
<style>
  :root {
    --orange: #F0912C;
    --orange-soft: #F2A743;
    --ink: #231f20;
    --white: #ffffff;
    --backdrop: #9b9b9b;
    --card-w: 880px;
    --card-h: 500px;
  }
  * { box-sizing: border-box; margin: 0; padding: 0; }
  html, body {
    width: 1074px;
    height: 1200px;
    overflow: hidden;
    background: var(--backdrop);
    font-family: "Montserrat", sans-serif;
  }
  .sheet {
    width: 1074px;
    height: 1200px;
    display: flex;
    flex-direction: column;
    align-items: center;
    justify-content: center;
    gap: 60px;
  }
  .card {
    position: relative;
    width: var(--card-w);
    height: var(--card-h);
    overflow: hidden;
  }

  /* Front */
  .card--front { background: var(--white); }
  .front__band {
    position: absolute;
    left: 0; right: 0;
    top: 33%;
    height: 27%;
    background: var(--orange);
  }
  .front__mark {
    position: absolute;
    left: 50%;
    top: 46.5%;
    width: 70px;
    height: 70px;
    transform: translate(-50%, -50%);
    background: var(--ink);
  }
  .front__rule {
    position: absolute;
    left: 0; right: 0;
    top: 65%;
    display: flex;
    align-items: center;
    gap: 18px;
    transform: translateY(-50%);
  }
  .front__rule::before,
  .front__rule::after {
    content: "";
    flex: 1;
    height: 4px;
    background: var(--ink);
  }
  .front__name {
    font-size: 27px;
    font-weight: 600;
    letter-spacing: 0.08em;
    color: var(--ink);
    white-space: nowrap;
  }

  /* Back */
  .card--back {
    background: var(--orange);
    color: var(--white);
    text-align: center;
  }
  .card--back::after {
    content: "";
    position: absolute;
    left: 0; right: 0; bottom: 0;
    height: 4%;
    background: var(--white);
  }
  .back__title {
    position: absolute;
    left: 0; right: 0;
    top: 9%;
  }
  .label-box {
    display: inline-block;
    background: var(--white);
    color: var(--orange);
    font-weight: 700;
    padding: 2px 12px;
  }
  .back__company { font-size: 32px; line-height: 1.2; }
  .back__company-sub {
    display: block;
    font-size: 30px;
    font-weight: 400;
    margin-top: 4px;
  }
  .back__contact {
    position: absolute;
    left: 28%; right: 28%;
    top: 34%;
    font-size: 20px;
    font-weight: 400;
  }
  .back__phones {
    display: flex;
    justify-content: center;
    gap: 26px;
    padding-bottom: 6px;
    border-bottom: 2px solid var(--white);
  }
  .back__email { margin-top: 8px; }
  .back__services-title {
    position: absolute;
    left: 0; right: 0;
    top: 57%;
  }
  .back__services-title .label-box { font-size: 32px; line-height: 1.25; }
  .services {
    position: absolute;
    left: 7%; right: 7%;
    top: 72%;
    display: grid;
    grid-template-columns: repeat(4, 1fr);
    font-size: 21px;
    font-weight: 400;
    list-style: none;
  }
  .services li { padding: 4px 0; }
  .services li:nth-child(-n+4) { border-bottom: 2px solid var(--white); padding-bottom: 10px; }
  .services li:nth-child(n+5) { padding-top: 10px; }
</style>
</head>
<body>
<main class="sheet">
  <section class="card card--front" aria-label="Card front">
    <div class="front__band"></div>
    <div class="front__mark"></div>
    <div class="front__rule">
      <span class="front__name">TRELLWICK CONSTRUCTION GROUP LTD</span>
    </div>
  </section>

  <section class="card card--back" aria-label="Card back">
    <div class="back__title">
      <span class="label-box back__company">Trellwick Construction</span>
      <span class="back__company-sub">Group Ltd</span>
    </div>
    <div class="back__contact">
      <div class="back__phones"><span>07931 258 904</span><span>07713829516</span></div>
      <div class="back__email">trellgroup@stonevane-mail.com</div>
    </div>
    <div class="back__services-title"><span class="label-box">Services</span></div>
    <ul class="services">
      <li>Groundworks</li>
      <li>Foundations</li>
      <li>Drainage</li>
      <li>Landscaping</li>
      <li>Patios</li>
      <li>Decking</li>
      <li>Fencing</li>
      <li>Hard Landscaping</li>
    </ul>
  </section>
</main>
</body>
</html>
```